Kestrel Bridge Consulting (KBC) Business Card Design

I would like to create double-sided business cards that contain:
1) Name: Derek Molvane
2) Phone Number: +1 (555) 218-4907
3) Email: Derek.Molvane@KestrelBridgeConsulting.example
4) Website: KestrelBridgeConsulting.example

I would like to include my logo and a color scheme similar to the Varnholt Grand Prix Ostera squad color scheme (black, silver, greenish-blue – but can also include regular blue)

What we do: Our company develops and delivers innovative and pragmatic information technology and cybersecurity risk and compliance solutions for organizations in the commercial market as well as the federal, and state/local sectors.

```html
<!DOCTYPE html>
<html lang="en">
<head>
<meta charset="utf-8">
<title>Kestrel Bridge Consulting – Business Card</title>
<link rel="stylesheet" href="https://fonts.googleapis.com/css2?family=Arimo:wght@400;700&family=Saira:wght@700&display=swap">
<style>
  :root {
    --canvas: #d9dce1;
    --navy: #0a0d22;
    --paper: #f3f4f6;
    --ink: #1f2430;
    --royal: #1d5fa8;
    --teal: #19c0c0;
    --cyan: #19d3ea;
    --blue: #1466d6;
    --rule: #2a2e38;
    --white: #ffffff;
  }
  * { box-sizing: border-box; margin: 0; padding: 0; }
  html, body { width: 1200px; height: 912px; overflow: hidden; }
  body {
    background: var(--canvas);
    font-family: "Arimo", Arial, sans-serif;
    display: flex; flex-direction: column; align-items: center; justify-content: center;
    gap: 56px;
  }
  .card {
    width: 620px; height: 354px; position: relative; overflow: hidden;
    box-shadow: 0 10px 28px rgba(10, 13, 34, 0.25);
  }

  /* Back side */
  .card-back { background: var(--navy); }
  .card-back .wordmark {
    position: absolute; left: 0; right: 0; top: 118px;
    display: flex; align-items: center; justify-content: center; gap: 16px;
  }
  .card-back .wordmark-dot {
    width: 30px; height: 30px; border-radius: 50%; background: var(--teal);
  }
  .card-back .wordmark-name {
    color: var(--teal); font-size: 30px; font-weight: 700; letter-spacing: 0.5px;
  }
  .card-back .web {
    position: absolute; left: 0; right: 0; bottom: 58px; text-align: center;
    color: var(--white); font-size: 13px; font-weight: 700; letter-spacing: 2.6px;
  }

  /* Front side */
  .card-front { background: var(--paper); }
  .front-mark {
    position: absolute; right: 70px; top: 38px;
    display: flex; align-items: center; gap: 12px;
  }
  .front-mark-dot { width: 34px; height: 34px; border-radius: 50%; background: var(--blue); }
  .front-mark-name {
    color: var(--ink); font-size: 15px; font-weight: 400; letter-spacing: 1.4px;
    line-height: 1.05; text-transform: uppercase;
    border-left: 1px solid var(--ink); padding-left: 8px;
  }
  .top-rule {
    position: absolute; left: 230px; right: 26px; top: 118px;
    height: 1px; background: var(--rule);
  }
  .identity { position: absolute; left: 36px; top: 186px; }
  .person-name {
    font-family: "Saira", "Arimo", sans-serif; font-weight: 700;
    color: var(--royal); font-size: 26px; letter-spacing: 0.4px; line-height: 1;
  }
  .person-title { color: var(--teal); font-size: 17px; margin-top: 3px; }
  .mid-rule {
    position: absolute; left: 36px; right: 150px; top: 244px;
    height: 1px; background: var(--rule);
  }
  .contacts { position: absolute; left: 36px; top: 254px; list-style: none; }
  .contacts li {
    display: flex; align-items: center; gap: 10px;
    color: var(--ink); font-size: 13.5px; line-height: 20px;
  }
  .contacts svg { width: 13px; height: 13px; fill: var(--royal); flex: none; }
  .bottom-band {
    position: absolute; left: 0; right: 0; bottom: 0; height: 18px; display: flex;
  }
  .band-gradient { flex: 1; background: linear-gradient(90deg, var(--blue), var(--cyan)); }
  .band-gap { width: 3px; background: var(--paper); }
  .band-dark { width: 112px; background: var(--navy); }
</style>
</head>
<body>

<section class="card card-back" aria-label="Card back">
  <div class="wordmark">
    <span class="wordmark-dot"></span>
    <span class="wordmark-name">Kestrel Bridge Consulting</span>
  </div>
  <p class="web">www.KestrelBridgeConsulting.example</p>
</section>

<section class="card card-front" aria-label="Card front">
  <div class="front-mark">
    <span class="front-mark-dot"></span>
    <span class="front-mark-name">Kestrel<br>Bridge<br>Consulting</span>
  </div>
  <div class="top-rule"></div>

  <div class="identity">
    <h1 class="person-name">DEREK MOLVANE</h1>
    <p class="person-title">President</p>
  </div>
  <div class="mid-rule"></div>

  <ul class="contacts">
    <li>
      <svg viewBox="0 0 24 24" aria-hidden="true"><path d="M6.6 10.8a15.1 15.1 0 0 0 6.6 6.6l2.2-2.2c.3-.3.7-.4 1-.2 1.1.4 2.3.6 3.6.6.6 0 1 .4 1 1V20c0 .6-.4 1-1 1A17 17 0 0 1 3 4c0-.6.4-1 1-1h3.5c.6 0 1 .4 1 1 0 1.3.2 2.5.6 3.6.1.3 0 .7-.2 1z"/></svg>
      +1 (555) 218-4907
    </li>
    <li>
      <svg viewBox="0 0 24 24" aria-hidden="true"><path d="M2 5h20v14H2z M2 5l10 8 10-8" /></svg>
      Derek.Molvane@KestrelBridgeConsulting.example
    </li>
    <li>
      <svg viewBox="0 0 24 24" aria-hidden="true"><circle cx="12" cy="12" r="10"/></svg>
      www.KestrelBridgeConsulting.example
    </li>
  </ul>

  <div class="bottom-band">
    <span class="band-gradient"></span>
    <span class="band-gap"></span>
    <span class="band-dark"></span>
  </div>
</section>

</body>
</html>
```